Brindle Chill Supplies Stationery Design

Stationery Design

Thank you to all those who have submitted the logos. We have selected the logo for our new identity and we are now looking for stationery ideas.

The attached logo must be used in all stationery designs.

We require the following items of stationery:

1. Business Cards for 10 employees – Double Sided – All the card will have the same address:

7 – 31 Marrowby Lane, Kingston Upon Thames, Surrey, KT4 9QX, United Kingdom

Office phone number: +44 (0)208 613 7742

Freephone: 0800 129 4837

Fax: +44 (0)20 8731 2964

Website: www.brindlechill.example

The names on the cards and mobile numbers – will be given on selection of final design.

A few of the cards will have different emails but 5/6 card will have the same email address.

2. Letterhead A4 – same contact details as above – email address to be used info@brindlechill.example

3. Compliments Slip – same details as no.2

4. Envelope designs – with just the address, Freephone and Website.

Sizes Required: C4 – 324mm x 229mm – Windows and Regular

DL – 110mm x 220mm – Windows and Regular

5. A4 Ring Binder – Logo at the front and back and side; company name on the front and side of the binder (Brindle Chill Supplies); contact details at the back; same as number 2 above.

The ring binder will have food, drink and hygiene inserts inside and will act as a temporary brochure.

It may help with the design process to know we sell a range of frozen food products including chips, burgers, fish, frozen poultry items, vegetables, ice cream, desserts, bakery products, pies, pasties, onion rings, pizza toppings etc.

We also sell ambient products such as sauces, crisps such as dunmores, chocolates such as Hollensby, Vorelle, Quib etc.

Drinks wise we sell branded products such as zesta tonic, fizmo, lumra, glint, sky hare etc; As well as juices and mineral water.

We also sell hygiene products such as tissue paper, hand towels, and other washroom products, bleaches etc.

Our website doesn’t have the full range of products but gives you a good idea of what we do www.brindlechill.example

Please note we are looking for a classy, slick design so don’t worry about trying to add all the products on the binder design; these have just been given to assist with the design process.

We may add a slogan to the stationery but the final decision on this still has to be taken and the profile will be updated within the next 72 hours.

This project will only last a maximum of 10-14 days, we don’t want to drag it out like the logo so please only submit creative ideas; which have been given thought in terms of design, text and graphics.

Any questions, feel free to ask.

Thank you and we look forward to your designs.

Regards

Torvin Ashcombe

I've uploaded an Adobe Illustrator CS2.ai file, and an EPS file of my new logo so you can get better clarity within your designs for this project

Thanks
Torvin

Hi

We have had various questions in respect of dimensions and budget; we have addressed both issues below by providing dimensions and we will be increasing the budget to $500 as soon as Pixel Bazaar let us know how we can increase; they have already been emailed.

In respect of the dimensions, we have had various answers but here are the most common sizes.

 

There are various sizes of lever arch A4 folders but the most common ones are below:

 

 

• Dimensions width 28.5cm, height 32cm,spine 9cm
• Dimensions (mm)H:315 x W:285
• Dimensions (mm) H:31cm x W:27cm

 

The most common thickness in the UK seems to be 70mm; so can we use this as a guide please.

 

 

Compliment Slip Sizes:

 

• Our Compliment Slips are DL in size. You should design your Compliment Slip to DL dimension but also add a 3mm bleed around each edge.

 

Trim Size – 99mm x 210mm

 

With Bleed – 105mm – 216mm

 

 

Business Cards:

 

Trim Size: 85mm x 55mm

 

With Bleed: 91mm x 61mm

 

 

We have extended the time frame and the budget on this so look forward to new designs.

 

I hope this helps and all the best for Christmas and 2010..

 

Regards

Torvin Ashcombe.

Hi Guys

Another important point to mention as each country has different rules...

In the Uk the postage stamps go in the top right hand corner of the envelope so we will have to have our logo company details etc in either the top left or the bottom of the envelope.

Also all envelopes must have at the back our return address:

Return Address:

Brindle Chill Supplies Ltd
7 - 31 Marrowby Lane
Kingston Upon Thames
Surrey
KT4 9QX

So we could even have the business logo, name and website address at the front and the address at the back.

Regards

Torvin

```html
<!DOCTYPE html>
<html lang="en">
<head>
<meta charset="utf-8">
<title>Brindle Chill Supplies – Stationery</title>
<link rel="stylesheet" href="https://fonts.googleapis.com/css2?family=Source+Sans+3:wght@400;600;700&display=swap">
<style>
  :root {
    --navy: #2a2e78;
    --red: #b3202a;
    --ink: #111111;
    --edge: #333333;
    --paper: #ffffff;
    --mark: #3b3f8c;
  }
  * { box-sizing: border-box; margin: 0; padding: 0; }
  html, body { width: 1200px; height: 847px; overflow: hidden; background: var(--paper); }
  body { font-family: "Source Sans 3", "Myriad Pro", Arial, sans-serif; color: var(--navy); }

  .canvas { position: relative; width: 1200px; height: 847px; overflow: hidden; }
  .sheet {
    position: absolute; left: 0; top: 0;
    width: 1306px; height: 922px;
    transform: scale(0.91884, 0.91865);
    transform-origin: 0 0;
  }

  .envelope, .card {
    position: absolute; background: var(--paper);
    border: 1px solid var(--edge);
  }
  .envelope svg.flap { position: absolute; left: 0; top: 0; overflow: visible; }

  .envelope--c4 { left: 0; top: 0; width: 651px; height: 921px; }
  .envelope--dl { left: 681px; top: 0; width: 625px; height: 313px; }

  .corner-mark { position: absolute; }

  .return-address {
    position: absolute; width: 260px; margin-left: -130px;
    text-align: center; font-size: 13.5px; line-height: 14.3px; color: var(--navy);
  }
  .return-address .heading { font-weight: 700; }

  .card { width: 253px; height: 145px; }
  .card--front { left: 732px; top: 379px; }
  .card--back { left: 1015px; top: 378px; }

  .card-brand { position: absolute; display: flex; align-items: center; color: var(--ink); }
  .card--front .card-brand { left: 10px; top: 12px; gap: 12px; }
  .card--front .brand-name { font-size: 24px; line-height: 23px; font-weight: 600; }
  .card--back .card-brand { left: 10px; top: 8px; gap: 6px; }
  .card--back .brand-name { font-size: 11.5px; line-height: 12px; font-weight: 600; }

  .contact-name {
    position: absolute; left: 0; right: 0; top: 98px; text-align: center;
    color: var(--red); font-size: 18px; font-variant: small-caps; letter-spacing: 0.2px;
  }

  .card-address {
    position: absolute; right: 8px; top: 4px; text-align: right;
    font-size: 9.5px; line-height: 12px; color: var(--navy);
  }
  .card-phones {
    position: absolute; left: 0; right: 0; top: 66px; text-align: center;
    font-size: 9.5px; line-height: 11.5px; color: var(--navy);
  }
  .card-phones .label, .card-footer .label { color: var(--red); }
  .card-footer {
    position: absolute; left: 5px; right: 8px; top: 126px;
    display: flex; justify-content: space-between;
    font-size: 9.5px; color: var(--navy);
  }
</style>
</head>
<body>
<div class="canvas">
  <div class="sheet">

    <!-- C4 envelope, back -->
    <section class="envelope envelope--c4" aria-label="C4 envelope back">
      <svg class="flap" width="651" height="921" viewBox="0 0 651 921">
        <polyline points="20,0 72,128 577,128 650,10" fill="none" stroke="#333" stroke-width="1"/>
      </svg>
      <svg class="corner-mark" style="left:38px;top:851px" width="54" height="54" viewBox="0 0 54 54">
        <circle cx="27" cy="27" r="25" fill="var(--mark)"/>
      </svg>
      <svg class="corner-mark" style="left:560px;top:851px" width="54" height="54" viewBox="0 0 54 54">
        <circle cx="27" cy="27" r="25" fill="var(--mark)"/>
      </svg>
      <div class="return-address" style="left:320px;top:846px">
        <div class="heading">RETURN ADDRESS</div>
        <div>Brindle Chill Supplies Ltd</div>
        <div>7 - 31 Marrowby Lane,</div>
        <div>Kingston Upon Thames,</div>
        <div>Surrey, KT4 9QX</div>
      </div>
    </section>

    <!-- DL envelope, back -->
    <section class="envelope envelope--dl" aria-label="DL envelope back">
      <svg class="flap" width="625" height="313" viewBox="0 0 625 313">
        <polyline points="0,0 59,78 564,78 624,0" fill="none" stroke="#333" stroke-width="1"/>
      </svg>
      <svg class="corner-mark" style="left:26px;top:239px" width="54" height="54" viewBox="0 0 54 54">
        <circle cx="27" cy="27" r="25" fill="var(--mark)"/>
      </svg>
      <svg class="corner-mark" style="left:548px;top:239px" width="54" height="54" viewBox="0 0 54 54">
        <circle cx="27" cy="27" r="25" fill="var(--mark)"/>
      </svg>
      <div class="return-address" style="left:308px;top:234px">
        <div class="heading">RETURN ADDRESS</div>
        <div>Brindle Chill Supplies Ltd</div>
        <div>7 - 31 Marrowby Lane,</div>
        <div>Kingston Upon Thames,</div>
        <div>Surrey, KT4 9QX</div>
      </div>
    </section>

    <!-- Business card, front -->
    <section class="card card--front" aria-label="Business card front">
      <div class="card-brand">
        <svg width="66" height="66" viewBox="0 0 66 66" aria-hidden="true">
          <circle cx="33" cy="33" r="32" fill="var(--mark)"/>
        </svg>
        <div class="brand-name">Brindle Chill<br>Supplies</div>
      </div>
      <div class="contact-name">Contact Name</div>
    </section>

    <!-- Business card, back -->
    <section class="card card--back" aria-label="Business card back">
      <div class="card-brand">
        <svg width="26" height="26" viewBox="0 0 26 26" aria-hidden="true">
          <circle cx="13" cy="13" r="12" fill="var(--mark)"/>
        </svg>
        <div class="brand-name">Brindle Chill<br>Supplies</div>
      </div>
      <div class="card-address">
        <div>7 - 31 Marrowby Lane,</div>
        <div>Kingston Upon Thames,</div>
        <div>Surrey, KT4 9QX</div>
      </div>
      <div class="card-phones">
        <div><span class="label">Office Phone:</span> +44 (0)208 613 7742</div>
        <div><span class="label">FreePhone:</span> 0800 129 4837</div>
        <div><span class="label">Fax:</span> +44 (0)20 8731 2964</div>
      </div>
      <div class="card-footer">
        <span>www.brindlechill.example</span>
        <span><span class="label">email:</span> info@brindlechill.example</span>
      </div>
    </section>

  </div>
</div>
</body>
</html>
```